Business Card Design Project- Removalist

I would like to surprise my husband to be with a different type of wedding present. His brother (who he owned a removalist business with) suddenly passed away from cancer recently and he has changed his business name to 'TQB' (which stands for Keeping Ted Strong; but the full name doesn't need to be on the business card as it is more of a personal business name). To celebrate the new business I would like to get him some business cards made.
I would like the business name to be listed as 'TQB' and somewhere on the card I would like 'Sydney wide removals and relocation services'. I would like it to be obvious from the front of the card that it is a removalist business card. If a truck or some other feature that makes it look like a removalist business card could added it would be appreciated.
I don't mind what colours are used, but I would like the colour blue to feature somewhere in the design. It can be bright and fun, which is how Ted was.
I will also need the company's email address and phone number listed
The email address is: tqbmoving@brisketmail.example
The contact number is: 0418 902 364
I don't need a contact name listed on the card, but perhaps 'Owned and operated by the Pemberton family' could be added near the contact details in small font.
Thank you very much for considering this project!
Kind regards,
Fiona
Updates
Could you please change the mobile contact number to 0418 902 364. This is the only contact phone number required on the card now.
Thank you!
Industry/Entity Type
Wedding
Look and feel
Each slider illustrates characteristics of the customer's brand and the style your logo design should communicate.

```html
<!DOCTYPE html>
<html lang="en">
<head>
<meta charset="utf-8">
<title>TQB Business Card</title>
<link rel="stylesheet" href="https://fonts.googleapis.com/css2?family=Open+Sans:wght@400;600;700&display=swap">
<style>
  :root {
    --page-bg: #e9e7e4;
    --label-bg: #111111;
    --label-text: #f5c230;
    --card-white: #f8f8f8;
    --card-grey: #d9d9d9;
    --road-dark: #160a06;
    --road-red: #7e160c;
    --road-glow: #f2a631;
    --truck-blue: #3a66c8;
    --box-brown: #8f7a6c;
    --fine-print: #6b6b6b;
  }
  html, body {
    margin: 0;
    width: 1200px;
    height: 1000px;
    overflow: hidden;
    background: var(--page-bg);
    font-family: "Open Sans", Arial, sans-serif;
  }
  .card-sheet {
    display: flex;
    flex-direction: column;
    align-items: center;
    justify-content: center;
    gap: 40px;
    height: 1000px;
  }
  .card {
    width: 760px;
    height: 456px;
    display: block;
    box-shadow: 0 6px 18px rgba(0,0,0,0.18);
  }
  .label-bar { fill: var(--label-bg); }
  .label-text {
    fill: var(--label-text);
    font-family: "Open Sans", Arial, sans-serif;
    font-weight: 700;
  }
  .label-icon { fill: var(--label-text); }
  .fine-print {
    fill: var(--fine-print);
    font-family: "Open Sans", Arial, sans-serif;
    font-weight: 400;
  }
  .light-streak {
    fill: none;
    stroke-linecap: round;
  }
</style>
</head>
<body>
<main class="card-sheet">

  <!-- Front -->
  <svg class="card card-front" viewBox="0 0 425 255" xmlns="http://www.w3.org/2000/svg">
    <defs>
      <linearGradient id="roadFront" x1="0" y1="0" x2="0.4" y2="1">
        <stop offset="0" stop-color="var(--road-red)"/>
        <stop offset="0.22" stop-color="#b8401a"/>
        <stop offset="0.38" stop-color="var(--road-glow)"/>
        <stop offset="0.55" stop-color="#4a1a0c"/>
        <stop offset="1" stop-color="var(--road-dark)"/>
      </linearGradient>
      <linearGradient id="panelFront" x1="0" y1="0" x2="0" y2="1">
        <stop offset="0" stop-color="var(--card-white)"/>
        <stop offset="1" stop-color="var(--card-grey)"/>
      </linearGradient>
      <radialGradient id="truckFront" cx="0.6" cy="0.55" r="0.6">
        <stop offset="0" stop-color="var(--truck-blue)"/>
        <stop offset="0.6" stop-color="var(--truck-blue)" stop-opacity="0.75"/>
        <stop offset="1" stop-color="var(--truck-blue)" stop-opacity="0"/>
      </radialGradient>
      <radialGradient id="boxesFront" cx="0.6" cy="0.55" r="0.6">
        <stop offset="0" stop-color="var(--box-brown)" stop-opacity="0.75"/>
        <stop offset="0.7" stop-color="var(--box-brown)" stop-opacity="0.45"/>
        <stop offset="1" stop-color="var(--box-brown)" stop-opacity="0"/>
      </radialGradient>
    </defs>
    <rect class="road-photo" width="425" height="255" fill="url(#roadFront)" role="img" aria-label="Photo of a highway at night with red and orange light trails"/>
    <path class="light-streak" d="M0 18 C90 10 200 6 300 2" stroke="#d2452a" stroke-width="2" opacity="0.6"/>
    <path class="light-streak" d="M0 60 C40 70 70 90 90 120" stroke="#ffd07a" stroke-width="1.4" opacity="0.5"/>
    <path class="white-panel" d="M305 0 C285 14 250 24 190 28 C120 32 92 55 80 95 C66 150 44 205 30 255 L425 255 L425 0 Z" fill="url(#panelFront)"/>
    <path class="light-streak" d="M200 118 L222 108" stroke="#ffffff" stroke-width="2" opacity="0.9"/>
    <ellipse class="truck-photo" cx="128" cy="92" rx="68" ry="52" fill="url(#truckFront)" role="img" aria-label="Photo of a blue removal truck driving along the highway"/>
    <ellipse class="boxes-photo" cx="362" cy="172" rx="70" ry="78" fill="url(#boxesFront)" role="img" aria-label="Photo of stacked cardboard moving boxes"/>
    <rect class="label-bar" x="230" y="153" width="70" height="20"/>
    <text class="label-text" x="237" y="168" font-size="12">TQB</text>
    <rect class="label-bar" x="100" y="192" width="238" height="18"/>
    <text class="label-text" x="105" y="204.5" font-size="7.6">Sydney wide removals and relocation services</text>
  </svg>

  <!-- Back -->
  <svg class="card card-back" viewBox="0 0 425 255" xmlns="http://www.w3.org/2000/svg">
    <defs>
      <linearGradient id="roadBack" x1="0" y1="0" x2="0.4" y2="1">
        <stop offset="0" stop-color="var(--road-red)"/>
        <stop offset="0.22" stop-color="#b8401a"/>
        <stop offset="0.38" stop-color="var(--road-glow)"/>
        <stop offset="0.55" stop-color="#4a1a0c"/>
        <stop offset="1" stop-color="var(--road-dark)"/>
      </linearGradient>
      <linearGradient id="panelBack" x1="0" y1="0" x2="0" y2="1">
        <stop offset="0" stop-color="var(--card-white)"/>
        <stop offset="1" stop-color="var(--card-grey)"/>
      </linearGradient>
      <radialGradient id="truckBack" cx="0.6" cy="0.55" r="0.6">
        <stop offset="0" stop-color="var(--truck-blue)"/>
        <stop offset="0.6" stop-color="var(--truck-blue)" stop-opacity="0.75"/>
        <stop offset="1" stop-color="var(--truck-blue)" stop-opacity="0"/>
      </radialGradient>
      <radialGradient id="boxesBack" cx="0.6" cy="0.55" r="0.6">
        <stop offset="0" stop-color="var(--box-brown)" stop-opacity="0.75"/>
        <stop offset="0.7" stop-color="var(--box-brown)" stop-opacity="0.45"/>
        <stop offset="1" stop-color="var(--box-brown)" stop-opacity="0"/>
      </radialGradient>
    </defs>
    <rect class="road-photo" width="425" height="255" fill="url(#roadBack)" role="img" aria-label="Photo of a highway at night with red and orange light trails"/>
    <path class="light-streak" d="M0 18 C90 10 200 6 300 2" stroke="#d2452a" stroke-width="2" opacity="0.6"/>
    <path class="light-streak" d="M0 60 C40 70 70 90 90 120" stroke="#ffd07a" stroke-width="1.4" opacity="0.5"/>
    <path class="white-panel" d="M305 0 C285 14 250 24 190 28 C120 32 92 55 80 95 C66 150 44 205 30 255 L425 255 L425 0 Z" fill="url(#panelBack)"/>
    <path class="light-streak" d="M200 118 L222 108" stroke="#ffffff" stroke-width="2" opacity="0.9"/>
    <ellipse class="truck-photo" cx="128" cy="92" rx="68" ry="52" fill="url(#truckBack)" role="img" aria-label="Photo of a blue removal truck driving along the highway"/>
    <ellipse class="boxes-photo" cx="362" cy="172" rx="70" ry="78" fill="url(#boxesBack)" role="img" aria-label="Photo of stacked cardboard moving boxes"/>

    <rect class="label-bar" x="185" y="152" width="116" height="20"/>
    <g class="label-icon phone-icon">
      <rect x="189" y="156" width="11" height="12" rx="2"/>
      <path d="M192 158.5 q-1 4 3 7 l1.5 -1.5 l2 1.5 l-1 1.2 q-6 -1 -7 -7.5 z" fill="var(--label-bg)"/>
    </g>
    <text class="label-text" x="204" y="166.5" font-size="11">0418 902 364</text>

    <rect class="label-bar" x="125" y="191" width="165" height="18"/>
    <g class="email-icon">
      <rect class="label-icon" x="130" y="195.5" width="11" height="8.5"/>
      <path d="M130 195.5 L135.5 200.5 L141 195.5" fill="none" stroke="var(--label-bg)" stroke-width="1"/>
    </g>
    <text class="label-text" x="145" y="203" font-size="6.9">tqbmoving@brisketmail.example</text>

    <text class="fine-print" x="126" y="222" font-size="6">Owned and operated by the Pemberton family</text>
  </svg>

</main>
</body>
</html>
```